Bref créative
Business Cards - Skyline Assessors
Two sided business cards
Simple
Corwin Hask
Certified Appraiser
48270 Millbrook Lane #1174
Sterling, VA 20391
corwin@plumvexa.com
www.plumvexa.com
Just the logo, either include the text or not (what ever looks better)
Colors and Fonts Guide

```html
<!DOCTYPE html>
<html lang="en">
<head>
<meta charset="utf-8">
<title>Skyline Assessors – Business Card</title>
<link href="https://fonts.googleapis.com/css2?family=PT+Sans:wght@400;700&family=PT+Serif&display=swap" rel="stylesheet">
<style>
  :root {
    --page-bg: #e6e4e1;
    --card-white: #ffffff;
    --brand-red: #c8102e;
    --red-bright: #e3262f;
    --red-deep: #8e0f1c;
    --wing-blue: #1d3f66;
    --wing-blue-light: #3f6f9e;
    --text-light: #ffffff;
  }
  html, body {
    margin: 0;
    padding: 0;
    width: 1200px;
    height: 780px;
    overflow: hidden;
    background: var(--page-bg);
  }
  .canvas {
    position: relative;
    width: 1200px;
    height: 780px;
    display: flex;
    align-items: center;
    justify-content: center;
  }
  .card {
    position: relative;
    width: 1100px;
    height: 640px;
    border-radius: 40px;
    overflow: hidden;
    background: var(--card-white);
    box-shadow: 0 10px 30px rgba(0,0,0,0.18);
  }
  .card-shape {
    position: absolute;
    inset: 0;
    width: 100%;
    height: 100%;
  }
  .brand-name {
    position: absolute;
    top: 112px;
    left: 0;
    width: 100%;
    text-align: center;
    margin: 0;
    font-family: "PT Sans", sans-serif;
    font-weight: 700;
    font-size: 66px;
    letter-spacing: 4px;
    text-transform: uppercase;
    color: var(--brand-red);
  }
  .holder {
    position: absolute;
    left: 150px;
    top: 385px;
    width: 340px;
    text-align: center;
    color: var(--text-light);
  }
  .holder-name {
    margin: 0;
    font-family: "PT Sans", sans-serif;
    font-weight: 700;
    font-size: 34px;
  }
  .holder-title {
    margin: 4px 0 0;
    font-family: "PT Sans", sans-serif;
    font-size: 27px;
  }
  .holder-address {
    margin: 14px 0 0 -40px;
    font-family: "PT Serif", serif;
    font-style: normal;
    font-size: 26px;
    line-height: 1.35;
    text-align: right;
    width: 380px;
  }
  .contact-list {
    position: absolute;
    left: 690px;
    top: 385px;
    margin: 0;
    padding: 0;
    list-style: none;
    font-family: "PT Serif", serif;
    font-size: 26px;
    color: var(--text-light);
  }
  .contact-item {
    display: flex;
    align-items: center;
    gap: 14px;
    height: 44px;
  }
  .contact-icon {
    width: 26px;
    height: 26px;
    flex: none;
  }
</style>
</head>
<body>
<main class="canvas">
  <article class="card">
    <svg class="card-shape" viewBox="0 0 1100 640" preserveAspectRatio="none" aria-hidden="true">
      <defs>
        <radialGradient id="redField" cx="50%" cy="60%" r="65%">
          <stop offset="0" stop-color="var(--red-bright)"/>
          <stop offset="0.6" stop-color="var(--brand-red)"/>
          <stop offset="1" stop-color="var(--red-deep)"/>
        </radialGradient>
        <linearGradient id="wingBand" x1="0" y1="0" x2="1" y2="0">
          <stop offset="0" stop-color="var(--wing-blue-light)"/>
          <stop offset="0.5" stop-color="var(--wing-blue)"/>
          <stop offset="1" stop-color="var(--wing-blue-light)"/>
        </linearGradient>
      </defs>
      <path class="red-field" fill="url(#redField)"
            d="M0,272 C250,292 450,372 550,520 C650,372 850,292 1100,272 L1100,640 L0,640 Z"/>
      <path class="wing-band" fill="url(#wingBand)"
            d="M0,262 C260,270 455,335 550,470 C645,335 840,270 1100,262 L1100,272 C850,292 650,372 550,520 C450,372 250,292 0,272 Z"/>
    </svg>

    <h1 class="brand-name">Skyline Assessors</h1>

    <section class="holder">
      <p class="holder-name">Corwin Hask</p>
      <p class="holder-title">Certified Appraiser</p>
      <address class="holder-address">48270 Millbrook Lane #1174<br>Sterling, VA 20391</address>
    </section>

    <ul class="contact-list">
      <li class="contact-item">
        <svg class="contact-icon" viewBox="0 0 24 24" aria-hidden="true">
          <circle cx="12" cy="12" r="12" fill="#fff"/>
          <rect x="8" y="4.5" width="8" height="15" rx="1.5" fill="var(--brand-red)"/>
          <rect x="9.5" y="6.5" width="5" height="8" fill="#fff"/>
        </svg>
        <span>5550148823</span>
      </li>
      <li class="contact-item">
        <svg class="contact-icon" viewBox="0 0 24 24" aria-hidden="true">
          <circle cx="12" cy="12" r="12" fill="#fff"/>
          <text x="12" y="16.5" text-anchor="middle" font-family="PT Sans, sans-serif" font-weight="700" font-size="14" fill="var(--brand-red)">@</text>
        </svg>
        <span>corwin@plumvexa.com</span>
      </li>
      <li class="contact-item">
        <svg class="contact-icon" viewBox="0 0 24 24" aria-hidden="true">
          <circle cx="12" cy="12" r="12" fill="#fff"/>
          <g fill="none" stroke="var(--brand-red)" stroke-width="1.5">
            <circle cx="12" cy="12" r="6.5"/>
            <ellipse cx="12" cy="12" rx="3" ry="6.5"/>
            <line x1="5.5" y1="12" x2="18.5" y2="12"/>
          </g>
        </svg>
        <span>www.plumvexa.com</span>
      </li>
    </ul>
  </article>
</main>
</body>
</html>
```